Marrowby's Vacation Rentals Business Card

Multi Million dollar villa rentals in the Dominican Republic.

Industry/Entity Type

Business

Contact Information for Business Card

I am looking for a high-end look around my company name/logo (see attached) on one side incorporating the following info: first and last name, title, address, phone #, email and company website. On the backside I want to add a full color picture of one of our villas (see attached).

```html
<!DOCTYPE html>
<html lang="en">
<head>
<meta charset="utf-8">
<title>Marrowby's Vacation Rentals – Business Card</title>
<link rel="stylesheet" href="https://fonts.googleapis.com/css2?family=Open+Sans:wght@400;600&display=swap">
<style>
  :root {
    --page-bg: #f1f1f1;
    --card-bg: #ffffff;
    --ink: #1f1f1f;
    --sun: #f07a2a;
    --panel: rgba(38, 38, 40, 0.78);
    --on-dark: #ffffff;
    --photo-sky: #8fb4d4;
    --photo-wall: #e9e4d8;
    --photo-shade: #7b7a6a;
    --photo-pool: #1d4f8a;
  }
  * { box-sizing: border-box; margin: 0; padding: 0; }
  html, body { width: 1200px; height: 1000px; overflow: hidden; }
  body {
    background: var(--page-bg);
    font-family: "Open Sans", Arial, sans-serif;
    position: relative;
  }
  .card {
    position: absolute;
    border-radius: 14px;
    overflow: hidden;
    box-shadow: 0 3px 8px rgba(0,0,0,0.22);
  }
  .card-front {
    left: 259px; top: 68px; width: 714px; height: 407px;
    background: var(--card-bg);
    display: flex; align-items: center; justify-content: center;
  }
  .brand {
    display: flex; align-items: center; gap: 20px;
    margin-top: -30px;
  }
  .brand-mark {
    width: 74px; height: 74px; border-radius: 50%;
    background: var(--sun);
    flex: none;
  }
  .brand-name {
    font-weight: 600;
    font-size: 42px;
    line-height: 1.15;
    color: var(--ink);
  }
  .card-back {
    left: 259px; top: 518px; width: 710px; height: 404px;
  }
  .villa-photo, .info-panel { position: absolute; inset: 0; }
  .contact-block {
    position: absolute; right: 14px; top: 0;
    text-align: right; color: var(--on-dark);
  }
  .person-name {
    position: absolute; right: 14px; top: 56px;
    font-size: 30px; font-weight: 600; letter-spacing: 0.5px;
    white-space: nowrap; color: var(--on-dark);
  }
  .person-title {
    position: absolute; right: 14px; top: 93px;
    font-size: 18px; white-space: nowrap; color: var(--on-dark);
  }
  .address {
    position: absolute; right: 10px; top: 177px;
    font-size: 18px; line-height: 25px; text-align: right;
    color: var(--on-dark); font-style: normal;
  }
  .contact-list {
    position: absolute; right: 6px; top: 244px;
    list-style: none; color: var(--on-dark);
  }
  .contact-list li {
    display: flex; align-items: center; justify-content: flex-end;
    gap: 18px; font-size: 18px; height: 29px;
  }
  .contact-list svg { width: 18px; height: 18px; flex: none; }
</style>
</head>
<body>

<section class="card card-front">
  <div class="brand">
    <span class="brand-mark" aria-hidden="true"></span>
    <span class="brand-name">Marrowby's<br>Vacation Rentals</span>
  </div>
</section>

<section class="card card-back">
  <svg class="villa-photo" width="710" height="404" viewBox="0 0 710 404" role="img" aria-label="Photo of a white villa with arched terrace, balustrade balcony, palm trees, sun loungers and a pool">
    <defs>
      <linearGradient id="villa-tones" x1="0" y1="0" x2="0" y2="1">
        <stop offset="0" stop-color="var(--photo-sky)"/>
        <stop offset="0.2" stop-color="var(--photo-wall)"/>
        <stop offset="0.7" stop-color="var(--photo-shade)"/>
        <stop offset="0.93" stop-color="var(--photo-wall)"/>
        <stop offset="1" stop-color="var(--photo-pool)"/>
      </linearGradient>
    </defs>
    <rect width="710" height="404" fill="url(#villa-tones)"/>
  </svg>

  <svg class="info-panel" width="710" height="404" viewBox="0 0 710 404" aria-hidden="true">
    <polygon points="466,0 356,197 451,404 710,404 710,0" fill="var(--panel)"/>
  </svg>

  <h1 class="person-name">DANIEL HART</h1>
  <p class="person-title">Ceo &amp; Founder</p>

  <address class="address">Your Street Address,<br>New York 12345</address>

  <ul class="contact-list">
    <li>+000 123 456 789
      <svg viewBox="0 0 24 24" fill="#fff"><path d="M6.6 10.8a15.1 15.1 0 0 0 6.6 6.6l2.2-2.2c.3-.3.7-.4 1-.2 1.1.4 2.3.6 3.6.6.6 0 1 .4 1 1V20c0 .6-.4 1-1 1A17 17 0 0 1 3 4c0-.6.4-1 1-1h3.5c.6 0 1 .4 1 1 0 1.3.2 2.5.6 3.6.1.3 0 .7-.2 1z"/></svg>
    </li>
    <li>daniel@marrowbysrentals.com
      <svg viewBox="0 0 24 24" fill="none" stroke="#fff" stroke-width="2"><rect x="2" y="5" width="20" height="14"/><path d="M2 5l10 8 10-8"/></svg>
    </li>
    <li>www.marrowbysrentals.com
      <svg viewBox="0 0 24 24" fill="none" stroke="#fff" stroke-width="1.8"><circle cx="12" cy="12" r="10"/><path d="M2 12h20M12 2c3 3 3 17 0 20M12 2c-3 3-3 17 0 20"/></svg>
    </li>
  </ul>
</section>

</body>
</html>
```